Modern Proposal / Estimate Template for Vehicle Wrap Company (Coat Comet)

Project Overview

We are looking for creative designers to develop a modern proposal / estimate template for our vehicle wrap company, Coat Comet.

This will be used repeatedly as our standard proposal format when presenting vehicle wrap projects to potential clients.

We are NOT looking for a basic invoice or QuickBooks-style estimate.

This should feel like a professional marketing piece that helps sell the project and impress the client.

What We Want

We want designers to propose new creative layout concepts using our logo and brand as the foundation, but we encourage original design ideas and graphics.

I am including some of logos and images for reference. You can also visit www.thecoatcomet.com to get a feel for our branding. We want you to use this as a baseline...but we are looking for fresh, new takes on our existing brand. Be creative please!

The final design should feel:

• Modern
• Bold
• Professional
• Clean
• Sales-focused

Think agency presentation rather than basic estimate document.

Template Purpose

The template should allow our team to easily customize proposals for each project.

The layout should include space for things like:

• Client logo
• Client company name
• Vehicle wrap mockups or design ideas
• Fleet details (vehicles, locations, logistics)
• Pricing breakdown

This template will be reused over and over, so the design should be structured but flexible.

Typical Proposal Sections

Design should allow space for sections like:

• Cover page
• Project overview
• Why work with Coat Comet
• Scope of work
• Vehicle / fleet breakdown
• Pricing / investment
• Next steps

You do not need to fill all content, but the layout should support these elements.

Creative Direction

We want designers to think about how to visually communicate:

• Vehicle branding
• Fleet marketing
• mobile advertising
• professional installation

Graphics, icons, and layout structure are where we are hoping to see creative input.

Important

Please do NOT simply recreate a basic estimate sheet.

We want creative concepts for a proposal layout that feels like a marketing presentation.

Designs that stand out visually while remaining clean and professional will be most successful.

Final Deliverable

A reusable proposal template layout that Coat Comet can customize for different clients and projects.

Editable design files preferred.

```html
<!DOCTYPE html>
<html lang="en">
<head>
<meta charset="utf-8">
<title>Coat Comet — Vehicle Wrap Proposal Template</title>
<link href="https://fonts.googleapis.com/css2?family=Bebas+Neue&family=Montserrat:wght@400;500;600;700&display=swap" rel="stylesheet">
<style>
:root{
  --backdrop:#3d3d3f;
  --red:#c9412a;
  --ink:#111112;
  --night:#161617;
  --paper:#d3d4d6;
  --rule:#8a8a8c;
  --white:#ffffff;
  --muted:#b9b9bb;
}
*{box-sizing:border-box;margin:0;padding:0}
html,body{width:938px;height:1200px;overflow:hidden;background:var(--backdrop)}
body{font-family:"Montserrat",sans-serif}
.board{position:absolute;left:0;top:0;width:1708px;height:2184px;transform:scale(0.5492);transform-origin:0 0}
.page{position:absolute;width:422px;height:597px;overflow:hidden;background:var(--paper);color:var(--ink);box-shadow:0 4px 14px rgba(0,0,0,.35)}
.page--dark{background:var(--night);color:var(--white)}
.abs{position:absolute}
.brand{position:absolute;top:30px;right:38px;font-family:"Bebas Neue",sans-serif;font-size:22px;line-height:1;letter-spacing:.5px;color:var(--ink)}
.page--dark .brand,.brand--light{color:var(--white)}
.heading{position:absolute;left:39px;font-family:"Bebas Neue",sans-serif;font-size:25px;line-height:1;letter-spacing:.2px}
.heading::after{content:"";position:absolute;left:0;bottom:-8px;width:52px;height:2px;background:var(--red)}
.copy{font-size:7.6px;line-height:1.45}
.photo{position:absolute}
.footer{position:absolute;left:0;right:0;bottom:0;height:20px;border-top:1px solid rgba(255,255,255,.7)}
.footer span{position:absolute;left:39px;top:5px;font-size:6px;letter-spacing:.3px;color:var(--white)}
.footer i{position:absolute;right:40px;top:-6px;width:11px;height:11px;border-radius:50%;background:var(--white)}
/* cover */
.cover-title{position:absolute;left:39px;top:90px;font-family:"Bebas Neue",sans-serif;font-size:47px;line-height:.9;color:var(--white)}
.cover-title em{font-style:normal;color:var(--red)}
.cover-rule{position:absolute;left:39px;top:180px;width:66px;height:2px;background:var(--red)}
.meta{position:absolute;left:39px;color:var(--white);font-size:8.5px;line-height:1.2}
.meta b{display:block;font-weight:700}
/* features */
.feature{position:absolute;width:160px}
.feature .dot{position:absolute;left:0;top:0;width:26px;height:26px;border-radius:50%;background:var(--red)}
.feature .dot svg{position:absolute;left:6px;top:6px}
.feature h4{margin-left:37px;font-family:"Bebas Neue",sans-serif;font-size:12.5px;font-weight:400;line-height:1}
.feature p{margin-left:37px;margin-top:3px;font-size:6.7px;line-height:1.35}
/* tables */
table{border-collapse:collapse;font-size:6.6px}
.grid{position:absolute;left:39px;width:345px}
.grid th{background:var(--ink);color:var(--white);font-weight:700;text-align:left;padding:0 9px;height:24px;font-size:6.3px;border:1px solid var(--ink)}
.grid td{border:1px solid #333;padding:0 9px;height:26px}
.logistics{position:absolute;left:39px;top:240px;width:345px;height:142px;border:1px solid #333}
.logistics .col{position:absolute;top:0;bottom:0}
.logistics .hd{height:24px;background:var(--ink);color:var(--white);font-weight:700;font-size:6.3px;padding:9px 9px 0}
.logistics .bd{padding:8px 9px;font-size:6.6px;line-height:1.3}
.logistics ul{list-style:none;margin-top:4px}
.logistics li{position:relative;padding-left:8px;margin-bottom:6px}
.logistics li::before{content:"•";position:absolute;left:0}
/* lists */
.bullets{list-style:none;font-size:7px}
.bullets li{position:relative;padding-left:8px;height:16.3px}
.bullets li::before{content:"•";position:absolute;left:0}
/* timeline */
.step{position:absolute;width:86px;height:77px;background:var(--ink);color:var(--white);padding:8px 9px;font-size:6.6px;line-height:1.15}
.step .ic{width:24px;height:24px;border:1px solid var(--white);border-radius:50%;margin-bottom:8px;position:relative}
.step .ic svg{position:absolute;left:5px;top:5px}
.step b{display:block;font-weight:700}
.price{position:absolute;left:39px;top:395px;width:344px;background:#d6d6d8;color:var(--ink)}
.price td{border:1px solid #9a9a9c;height:25.5px;padding:0 9px}
.price td:last-child{width:108px}
.price .total td{background:var(--red);color:var(--white);font-weight:700;border-color:var(--red)}
/* next steps */
.card{position:absolute;top:127px;width:98px;height:81px;background:var(--ink);border-radius:3px;color:var(--white);text-align:center;font-family:"Bebas Neue",sans-serif;font-size:12px;line-height:1.05;padding-top:32px}
.card .num{position:absolute;left:36px;top:-12px;width:26px;height:26px;border-radius:50%;background:var(--red);border:2px solid var(--white);font-size:17px;line-height:23px}
.note{position:absolute;left:39px;top:227px;width:345px;height:23px;border-radius:4px;background:var(--ink);color:var(--white);font-size:7px;text-align:center;line-height:23px}
/* back */
.contact{position:absolute;left:0;right:0;text-align:center;color:var(--white)}
</style>
</head>
<body>
<main class="board">

  <!-- Cover -->
  <section class="page page--dark" style="left:184px;top:161px">
    <div class="photo" role="img" aria-label="Dark photo of branded pickup trucks and a van parked in a row" style="inset:0;background:linear-gradient(180deg,#2a2a2b 0%,#3a3a3c 45%,#1c1c1d 75%)"></div>
    <svg class="abs" style="left:0;top:0" width="422" height="597" viewBox="0 0 422 597" aria-hidden="true">
      <polygon points="0,382 422,283 422,292 0,391" fill="#9c9ca0"/>
    </svg>
    <div class="photo" role="img" aria-label="Photo of a black wrapped delivery van driving on a city highway at dusk" style="left:0;top:0;width:422px;height:597px;clip-path:polygon(0 391px,422px 292px,422px 597px,0 597px);background:linear-gradient(180deg,#b9b0c2 45%,#8a8c93 62%,#4a4b50 80%,#2d2e31 100%)"></div>
    <div class="brand">COAT COMET</div>
    <h1 class="cover-title">Vehicle Wrap<br><em>Proposal</em></h1>
    <div class="cover-rule"></div>
    <div class="meta" style="top:211px"><b>PREPARED FOR</b>Birch Lane Plumbing</div>
    <div class="meta" style="top:249px"><b>PRESENTED BY</b>Coat Comet</div>
    <div class="meta" style="top:287px"><b>DATE</b>June 2026</div>
  </section>

  <!-- Overview -->
  <section class="page" style="left:643px;top:161px">
    <div class="photo" role="img" aria-label="Photo of white branded work trucks and a van on gravel" style="left:0;top:420px;width:422px;height:177px;background:linear-gradient(180deg,var(--paper) 0%,#b8b9bb 35%,#6c6d70 80%,#3a3a3c 100%)"></div>
    <div class="brand">COAT COMET</div>
    <h2 class="heading" style="top:74px">Project Overview</h2>
    <div class="abs copy" style="left:39px;top:112px;width:345px;text-align:justify">
      <p>This proposal outlines the design, production, and installation of custom vehicle wraps for Birch Lane Plumbing's service fleet.</p>
      <p style="margin-top:4px">Vehicle wraps transform your vehicles into highly visible mobile advertisements that promote your business wherever they travel. A professionally designed wrap strengthens brand recognition, builds customer trust, and generates new leads throughout your service area.</p>
      <p style="margin-top:4px">Coat Comet will manage the entire process—from concept and design to production and installation—to ensure your vehicles make a strong and lasting impression.</p>
    </div>
    <h2 class="heading" style="top:244px">Why Work With Coat Comet</h2>
    <div class="feature" style="left:39px;top:292px">
      <div class="dot"><svg width="14" height="14" viewBox="0 0 14 14" fill="none" stroke="#fff" stroke-width="1.3"><rect x="1.5" y="3" width="11" height="7" rx="1"/><circle cx="4" cy="11" r="1.5"/><circle cx="10" cy="11" r="1.5"/></svg></div>
      <h4>Fleet Branding Experts</h4>
      <p>We specialize in designing wraps for commercial vehicles and fleet branding.</p>
    </div>
    <div class="feature" style="left:212px;top:292px">
      <div class="dot"><svg width="14" height="14" viewBox="0 0 14 14" fill="none" stroke="#fff" stroke-width="1.3"><rect x="1.5" y="2" width="11" height="8" rx="1"/><path d="M5 13h4M7 10v3M4.5 7.5l4-4"/></svg></div>
      <h4>Custom Design Approach</h4>
      <p>Our design team creates graphics that maximize visibility and brand recognition.</p>
    </div>
    <div class="feature" style="left:39px;top:359px">
      <div class="dot"><svg width="14" height="14" viewBox="0 0 14 14" fill="none" stroke="#fff" stroke-width="1.3"><path d="M2 12l6-6M9 2l3 3-2 2-3-3zM2 2l10 10"/></svg></div>
      <h4>Professional Installation</h4>
      <p>Our experienced installers ensure precision application and long-lasting results.</p>
    </div>
    <div class="feature" style="left:212px;top:359px">
      <div class="dot"><svg width="14" height="14" viewBox="0 0 14 14" fill="none" stroke="#fff" stroke-width="1.3"><circle cx="7" cy="5.5" r="4"/><path d="M2 13h10M7 3.5v4"/></svg></div>
      <h4>Mobile Advertising Impact</h4>
      <p>Vehicle wraps generate thousands of impressions every day, making them one of the most cost-effective.</p>
    </div>
    <div class="footer"><span>VEHICLE WRAP PROPOSAL</span><i></i></div>
  </section>

  <!-- Fleet -->
  <section class="page" style="left:1101px;top:161px">
    <div class="photo" role="img" aria-label="Photo of four black branded vans parked in front of a brick workshop" style="left:0;top:410px;width:422px;height:187px;background:linear-gradient(180deg,var(--paper) 0%,#a9a9ab 20%,#7a5a4a 45%,#2a2a2c 75%,#4a4a4c 100%)"></div>
    <div class="brand">COAT COMET</div>
    <h2 class="heading" style="top:74px">Fleet / Vehicle Breakdown</h2>
    <table class="grid" style="top:113px">
      <tr><th style="width:143px">VEHICLE TYPE</th><th style="width:101px">QUANTITY</th><th>WRAP TYPE</th></tr>
      <tr><td>Van Wraps</td><td>5</td><td>Full Wrap</td></tr>
      <tr><td>Truck Wraps</td><td>3</td><td>Partial Wrap</td></tr>
      <tr><td>Trailer Wraps</td><td>2</td><td>Lettering</td></tr>
    </table>
    <div class="logistics">
      <div class="col" style="left:0;width:194px;border-right:1px solid #333">
        <div class="hd">INSTALLATION LOGISTICS</div>
        <div class="bd">Coat Comet will coordinate installation scheduling to minimize vehicle downtime.
          <ul>
            <li>Vehicles will be wrapped in scheduled batches</li>
            <li>Installation will take approximately 1–2 days per vehicle</li>
            <li>Fleet scheduling will be coordinated with your team</li>
          </ul>
        </div>
      </div>
      <div class="col" style="left:194px;right:0">
        <div class="hd">VEHICLE LOCATIONS</div>
        <div class="bd">Primary Location<br>Birch Lane Plumbing Headquarters<br>Millbrook, Texas</div>
      </div>
    </div>
    <div class="footer"><span>VEHICLE WRAP PROPOSAL</span><i></i></div>
  </section>

  <!-- Design ideas / scope -->
  <section class="page page--dark" style="left:184px;top:792px">
    <div class="brand">COAT COMET</div>
    <h2 class="heading" style="top:74px">Design Ideas</h2>
    <div class="photo" role="img" aria-label="Wrap mockup of a blue and red van with a bold brand graphic" style="left:39px;top:115px;width:345px;height:161px;background:linear-gradient(180deg,#d8d8da 0%,#d8d8da 15%,#3a4fb0 35%,#c33a34 60%,#d8d8da 85%)"></div>
    <div class="abs" style="left:39px;top:290px;font-size:7.2px;font-weight:600">Bold Brand Visibility</div>
    <ul class="abs bullets" style="left:39px;top:306px;width:345px">
      <li>This concept emphasizes large, high-contrast branding</li>
      <li>with bold typography and simplified graphics so the</li>
      <li>brand is easily visible from a distance.</li>
    </ul>
    <h2 class="heading" style="top:376px">Scope of Work</h2>
    <div class="abs" style="left:39px;top:414px;font-size:7px;font-weight:700">Coat Comet will provide full-service vehicle wrap production including:</div>
    <ul class="abs bullets" style="left:39px;top:430px;width:345px">
      <li>Custom vehicle wrap design</li>
      <li>Design revisions and approvals</li>
      <li>High-resolution vinyl printing</li>
      <li>Premium automotive-grade vinyl materials</li>
      <li>Surface preparation and cleaning</li>
      <li>Professional installation</li>
      <li>Quality inspection and finishing</li>
    </ul>
    <div class="footer"><span>VEHICLE WRAP PROPOSAL</span><i></i></div>
  </section>

  <!-- Timeline / pricing -->
  <section class="page page--dark" style="left:643px;top:792px">
    <div class="abs" style="left:0;top:0;width:422px;height:307px;background:var(--paper)"></div>
    <div class="brand">COAT COMET</div>
    <h2 class="heading" style="top:74px;color:var(--ink)">Project Timeline</h2>
    <div class="step" style="left:39px;top:122px">
      <div class="ic"><svg width="12" height="12" viewBox="0 0 12 12" fill="none" stroke="#fff" stroke-width="1"><rect x="1" y="1.5" width="10" height="7"/><path d="M4 11h4M6 8.5V11"/></svg></div>
      <b>Design<br>Development</b>Week 1
    </div>
    <div class="step" style="left:125px;top:198px">
      <div class="ic"><svg width="12" height="12" viewBox="0 0 12 12" fill="none" stroke="#fff" stroke-width="1"><rect x="1" y="4" width="10" height="5"/><rect x="3" y="1" width="6" height="3"/><rect x="3" y="8" width="6" height="3"/></svg></div>
      <b>Production<br>&amp; Printing</b>Week 2
    </div>
    <div class="step" style="left:211px;top:122px">
      <div class="ic"><svg width="12" height="12" viewBox="0 0 12 12" fill="none" stroke="#fff" stroke-width="1"><path d="M1 11l5-5M7 1l4 4-2 2-4-4zM1 1l10 10"/></svg></div>
      <b>Installation<br>Scheduling</b>Week 3
    </div>
    <div class="step" style="left:297px;top:198px">
      <div class="ic"><svg width="12" height="12" viewBox="0 0 12 12" fill="none" stroke="#fff" stroke-width="1"><circle cx="6" cy="6" r="5"/><path d="M3.5 6l2 2 3-4"/></svg></div>
      <b>Wrap<br>Installation</b>Week 4
    </div>
    <svg class="abs" style="left:0;top:0" width="422" height="307" viewBox="0 0 422 307" fill="none" stroke="#222" stroke-width="1" aria-hidden="true">
      <path d="M131 140 C160 145,175 160,182 182"/><path d="M178 178l4 5 2-6"/>
      <path d="M217 262 C240 255,262 235,268 212"/><path d="M265 216l3-5 3 5"/>
      <path d="M303 140 C330 145,345 160,352 182"/><path d="M348 178l4 5 2-6"/>
    </svg>
    <h2 class="heading" style="top:348px">Pricing / Investment</h2>
    <table class="price">
      <tr><td>Design Services</td><td>$1,200</td></tr>
      <tr><td>Vinyl Printing</td><td>$4,800</td></tr>
      <tr><td>Installation</td><td>$2,400</td></tr>
      <tr class="total"><td>Total Investment</td><td>$8,400</td></tr>
    </table>
    <div class="footer"><span>VEHICLE WRAP PROPOSAL</span><i></i></div>
  </section>

  <!-- Next steps -->
  <section class="page page--dark" style="left:1101px;top:792px">
    <div class="abs" style="left:0;top:0;width:422px;height:302px;background:var(--paper)"></div>
    <div class="photo" role="img" aria-label="Studio photo of a black branded cargo van with orange wheels" style="left:0;top:302px;width:422px;height:275px;background:radial-gradient(ellipse at 50% 55%,#3a3a3c 0%,#1c1c1d 55%,#0d0d0e 100%)"></div>
    <div class="brand">COAT COMET</div>
    <h2 class="heading" style="top:74px;color:var(--ink)">Next Steps</h2>
    <div class="card" style="left:39px"><span class="num">1</span>Review and<br>approve this<br>proposal</div>
    <div class="card" style="left:162px"><span class="num">2</span>Coat Comet<br>begins the<br>design process</div>
    <div class="card" style="left:286px"><span class="num">3</span>Installation<br>schedule is<br>confirmed</div>
    <div class="note">Our team will coordinate every step to ensure a smooth and efficient project.</div>
    <div class="footer"><span>VEHICLE WRAP PROPOSAL</span><i></i></div>
  </section>

  <!-- Back cover -->
  <section class="page page--dark" style="left:643px;top:1426px;background:radial-gradient(ellipse at 50% 35%,#1e1e1f 0%,#111112 70%)">
    <div class="abs" style="left:0;right:0;top:228px;text-align:center;font-family:'Bebas Neue',sans-serif;font-size:40px;line-height:1;color:var(--white)">COAT COMET</div>
    <div class="contact" style="top:491px;font-family:'Bebas Neue',sans-serif;font-size:30px;line-height:1">555-014-2290</div>
    <div class="contact" style="top:527px;font-size:8.5px">sales@thecoatcomet.com</div>
    <div class="contact" style="top:545px;font-size:8.5px">www.thecoatcomet.com</div>
  </section>

</main>
</body>
</html>
```